RW Marlo Building Company LLC
Residential and Commercial Construction
I need double sided standard sized Business Card [3.5" x 2"]
Designer to decide.
Professional
Kevin R. Darrow
4815 Brindlecove Road
Fernhollow, NC 28990
rw@rwmbuilding.example
My personal name does not need to be on the card or stationary since it is used in the company name.
New Home Construction,
Remodeling,
Room Additions,
Commercial Construction and Upfits,
Personalized Project Management

```html
<!DOCTYPE html>
<html lang="en">
<head>
<meta charset="utf-8">
<title>RW Marlo Building Company LLC – Business Card</title>
<link rel="stylesheet" href="https://fonts.googleapis.com/css2?family=Tinos:wght@400&family=Arimo:wght@700&display=swap">
<style>
  :root {
    --page-bg: #e9e6e2;
    --card-white: #ffffff;
    --card-light: #f1f1f1;
    --ink-dark: #2d2d2d;
    --text-light: #f4f4f4;
    --text-muted: #d9d9d9;
  }
  * { margin: 0; padding: 0; box-sizing: border-box; }
  html, body {
    width: 1200px; height: 780px; overflow: hidden;
    background: var(--page-bg);
  }
  .canvas { position: relative; width: 1200px; height: 780px; }
  .business-card {
    position: absolute; left: 100px; top: 104px;
    width: 1000px; height: 572px;
    border-radius: 36px; overflow: hidden;
    background: linear-gradient(180deg, var(--card-white) 0%, var(--card-light) 50%);
    box-shadow: 0 10px 30px rgba(0,0,0,0.25);
  }
  .card-waves { position: absolute; inset: 0; width: 100%; height: 100%; }
  .company-name {
    position: absolute; left: 440px; top: 118px; width: 520px;
    text-align: center;
    font-family: "Tinos", serif; font-weight: 400;
    font-size: 44px; line-height: 1.15;
    color: var(--ink-dark);
  }
  .contact-block {
    position: absolute; left: 52px; top: 338px;
    color: var(--text-light);
  }
  .person-name {
    font-family: "Arimo", sans-serif; font-weight: 700;
    font-size: 30px; line-height: 1.2; margin-bottom: 22px;
  }
  .address {
    font-family: "Tinos", serif; font-size: 22px; line-height: 1.3;
    color: var(--text-muted);
  }
  .contact-row {
    display: flex; gap: 26px; margin-top: 12px;
    font-family: "Tinos", serif; font-size: 21px; line-height: 1.25;
    color: var(--text-muted);
  }
  .address + .contact-row { margin-top: 24px; }
  .contact-item { display: flex; align-items: center; gap: 8px; }
  .contact-icon { width: 19px; height: 19px; fill: var(--text-light); }
</style>
</head>
<body>
<main class="canvas">
  <section class="business-card" aria-label="Business card front">
    <svg class="card-waves" viewBox="0 0 1000 572" preserveAspectRatio="none" aria-hidden="true">
      <defs>
        <linearGradient id="panelFill" x1="0" y1="0" x2="0" y2="1">
          <stop offset="0" stop-color="#3a3a3a"/>
          <stop offset="1" stop-color="#0c0c0c"/>
        </linearGradient>
        <linearGradient id="redFill" x1="0" y1="0" x2="1" y2="0">
          <stop offset="0" stop-color="#a3121a"/>
          <stop offset="0.55" stop-color="#8a0f16"/>
          <stop offset="1" stop-color="#5e0a0e" stop-opacity="0"/>
        </linearGradient>
        <linearGradient id="greyFill" x1="0" y1="0" x2="1" y2="0">
          <stop offset="0" stop-color="#9a9a9a" stop-opacity="0"/>
          <stop offset="0.6" stop-color="#8a8a8a"/>
          <stop offset="1" stop-color="#6a6a6a"/>
        </linearGradient>
      </defs>
      <path d="M0 268 C 220 248, 420 262, 620 300 C 780 330, 900 320, 1000 288 L1000 316 C 880 352, 760 352, 600 322 C 420 290, 220 290, 0 312 Z" fill="url(#redFill)"/>
      <path d="M380 282 C 560 300, 760 336, 1000 262 L1000 280 C 780 350, 560 322, 380 282 Z" fill="url(#greyFill)"/>
      <path d="M0 312 C 220 290, 420 290, 600 322 C 760 352, 880 352, 1000 316 L1000 572 L0 572 Z" fill="url(#panelFill)"/>
    </svg>

    <h1 class="company-name">RW Marlo Building<br>Company LLC</h1>

    <div class="contact-block">
      <p class="person-name">Kevin R. Darrow</p>
      <p class="address">4815 Brindlecove Road<br>Fernhollow, NC 28990</p>
      <div class="contact-row">
        <span class="contact-item">
          <svg class="contact-icon" viewBox="0 0 24 24" aria-hidden="true"><path d="M6.6 10.8a15 15 0 0 0 6.6 6.6l2.2-2.2c.3-.3.7-.4 1-.2 1.1.4 2.3.6 3.6.6.6 0 1 .4 1 1V20c0 .6-.4 1-1 1A17 17 0 0 1 3 4c0-.6.4-1 1-1h3.5c.6 0 1 .4 1 1 0 1.3.2 2.5.6 3.6.1.3 0 .7-.2 1z"/></svg>
          555-014-2201
        </span>
        <span class="contact-item">
          <svg class="contact-icon" viewBox="0 0 24 24" aria-hidden="true"><path d="M6 3h12v6H6zM4 10h16v8h-3v3H7v-3H4zM9 15v4h6v-4z"/></svg>
          555-014-2287
        </span>
      </div>
      <div class="contact-row">
        <span class="contact-item">
          <svg class="contact-icon" viewBox="0 0 24 24" aria-hidden="true"><path d="M12 2a10 10 0 1 0 5 18.7l-.9-1.7A8 8 0 1 1 20 12v1a2 2 0 0 1-4 0V7h-2v1a5 5 0 1 0 .7 7.3A4 4 0 0 0 22 13v-1A10 10 0 0 0 12 2zm0 13a3 3 0 1 1 0-6 3 3 0 0 1 0 6z"/></svg>
          rw@rwmbuilding.example
        </span>
        <span class="contact-item">
          <svg class="contact-icon" viewBox="0 0 24 24" aria-hidden="true"><path d="M12 2a10 10 0 1 0 0 20 10 10 0 0 0 0-20zm6.9 6h-3a15 15 0 0 0-1.3-3.9A8 8 0 0 1 18.9 8zM12 4c.8 1.2 1.5 2.5 1.9 4h-3.8c.4-1.5 1.1-2.8 1.9-4zM4.3 14a8 8 0 0 1 0-4h3.4a16 16 0 0 0 0 4zm.8 2h3a15 15 0 0 0 1.3 3.9A8 8 0 0 1 5.1 16zm3-8h-3a8 8 0 0 1 4.3-3.9C8.8 5.3 8.4 6.6 8.1 8zM12 20c-.8-1.2-1.5-2.5-1.9-4h3.8c-.4 1.5-1.1 2.8-1.9 4zm2.3-6H9.7a14 14 0 0 1 0-4h4.6a14 14 0 0 1 0 4zm.3 5.9c.6-1.2 1-2.5 1.3-3.9h3a8 8 0 0 1-4.3 3.9zm1.7-5.9a16 16 0 0 0 0-4h3.4a8 8 0 0 1 0 4z"/></svg>
          www.rwmbuilding.example
        </span>
      </div>
    </div>
  </section>
</main>
</body>
</html>
```